Photography Company Seeks Amazing and Fun Website Design

Note: This is for design only. No coding required. We want to see your ideas for a great website! This will be a FUN design and not boring like others you may work on.

Please let your creative ideas flow. We have given you a ton of info along with videos to help you understand what we are after, however we WANT your creativity to shine through in your designs!

We are a professional company that has run hundreds of crowdsourced projects on multiple platforms. If you participate in this contest (we hope you do) you can expect great video feedback, consistent feedback, and also our guarantee that if we know your website design will not be what we are looking for we will notify you so you don’t waste your time if there is no chance of you winning.

We respect and recognize this is how you make your living and we will not play games. We look forward to an awesome contest and awesome website designs.

Design Brief:

We are looking for a stunning website design to showcase this amazing photography company. Their current site is:

http://www.kelvaprints.example/

As you can see they do amazing photography and need an amazing website to showcase their work and to attract new people into their studios.

We are looking to get a website that is clean, classy, bright, artistic, and that really helps this company stand out amongst other photography companies.

We need a homepage and an interior page mockup.

Here are some examples of other sites in their business with what we like:

http://www.tabrowenstudio.example/

Please watch video to learn what we like and don’t like:http://clipvault.example/t/QpR4sz7LmWd

http://www.holbrinkimaging.example/

Please watch video to learn what we like and don’t like: http://clipvault.example/t/Hb8ufN2kxyPa

NOTE: We do not want to copy anything outright. We want to learn, model and take their ideas and make them better. We also want to be flexible and take what we like along with your creativity to make an amazing design.

Here is what we are looking for in more specific terms:

NOTE: Website should have a spot for video on the homepage.

This website is for a very professional and well know photography company. Because it is photography the website needs to be VERY visual.

Site should be unique and really stand out to help sell the business and their services. EVERYTHING about this business is visual, so the site MUST reflect that.

Site Overall: Fun and Artistic. This is a forward thinking company that is fun, upbeat, and does things differently, they need the design to reflect that. This is a modern photography company.

They also do all kinds of photography from school kids, sports teams, in studio shoots with High School Seniors, Family Pictures etc.

Colors: We like the white background because it is clean and really helps the photos stand out. Also please look at the logo too. Use colors from that and make things flow. Again we want this to stand out and be different while at the same time being clean.

Menu: Horizontal. We like bold and easy to read menu items. Don’t make it small and cluttered. Include the same items that are in the other site for the mock up.

Site Structure: Clean and easy to navigate. We have a lot of content to display so we need a clean structure that breaks up the text and content areas.

Images: Please pull images from the current site. We can always replace the images of course, but if you show them “their own stuff” in the new design you will be closer to winning because it will feel more like “them”

Content Areas: It is a safe bet that if it is on the current site we need it on the new site. So don’t drop anything as it makes it hard to “cut content”.

What we don't want: We do not want clutter, boring, or templates or themes. We don’t want too cartoony, too cute, or too fancy. We don’t want ugly.

Out of respect to professional designers who really are working hard to win if you do not follow this brief, you submit worn out themes, templates, or boring designs you will be eliminated. We are offering great prize money for this so we expect great visual designs.

Thanks,

The Solvane Team

Target Market(s)

Target Market are upper middle class who want a better photography studio then the average studio, but don't want to go to the highest end of photography. This studio will cater to higher middle class.

Industry/Entity Type

Business

Number of Pages Required

1 page

Font styles to use
Sans Serif

Requirements
Must have
• Video on Home page
• Clean
• Stand Out
• Fun
• Professional
Nice to have
• Creative
• Lots of content in a great structure
Should not have
• clutter
• ugly design
• messy

```html
<!DOCTYPE html>
<html lang="en">
<head>
<meta charset="utf-8">
<title>Kelva Prints – Specials</title>
<link rel="stylesheet" href="https://fonts.googleapis.com/css2?family=Josefin+Sans:ital,wght@0,300;0,400;0,600;1,400&display=swap">
<style>
:root{
  --page:#eeeeee;
  --white:#ffffff;
  --ink:#333333;
  --body:#444444;
  --muted:#8c8c8c;
  --accent:#e8481a;
  --accent-dark:#d33c10;
  --footer:#2a2a2a;
  --footer-text:#5a5a5a;
  --icon:#6a6a6a;
}
*{box-sizing:border-box;margin:0;padding:0}
html,body{width:1039px;height:1200px;overflow:hidden}
body{background:var(--page);font-family:"Josefin Sans",sans-serif;color:var(--body);position:relative}
.abs{position:absolute}
.header{left:81px;top:0;width:877px;height:71px;background:var(--white)}
.brand{left:82px;top:14px;font-size:34px;font-weight:400;color:#111;display:flex;align-items:center;gap:8px}
.brand-dot{width:20px;height:20px;border-radius:50%;background:var(--accent)}
.social-top{top:9px;width:17px;height:17px}
.nav a{position:absolute;top:43px;font-size:12px;font-weight:600;letter-spacing:.6px;color:var(--ink);text-decoration:none}
.nav .active::after{content:"";position:absolute;left:-5px;right:-5px;top:27px;height:2px;background:var(--accent)}
.dropdown{left:416px;top:73px;width:126px;height:125px;background:var(--white);box-shadow:0 1px 4px rgba(0,0,0,.15);z-index:2}
.dropdown a{position:absolute;left:13px;font-size:10px;color:var(--body);text-decoration:none}
.dropdown .current{color:var(--accent)}
.tagline{left:80px;top:99px;font-size:29px;font-weight:600;color:var(--muted);letter-spacing:.5px;white-space:nowrap}
.follow{left:750px;top:81px;width:205px;height:31px;border:1px solid #d0d0d0;border-radius:16px;background:var(--white);font-size:13px;color:#555;padding:8px 0 0 20px}
.follow-square{position:absolute;right:12px;top:4px;width:21px;height:21px;border-radius:3px;background:#6b4f3a}
.cta{background:linear-gradient(#f0601f,var(--accent-dark));color:var(--white);border-radius:3px;line-height:1.25}
.cta-top{left:81px;top:146px;width:193px;height:55px;padding:10px 0 0 19px;font-size:14px}
.cta-top b{font-size:15px;letter-spacing:1px}
.cta-foot{left:811px;top:1054px;width:147px;height:41px;padding:7px 0 0 15px;font-size:10.5px}
.cta-foot b{font-size:11px;letter-spacing:1px}
.page-title{left:0;width:1047px;top:261px;text-align:center;font-size:19px;font-weight:600;color:var(--ink);text-decoration:underline;text-underline-offset:3px;letter-spacing:.5px}
.content{left:144px;top:0;width:690px}
.section-title{position:absolute;font-size:16.5px;font-weight:400;color:var(--ink);white-space:nowrap}
.content p{position:absolute;font-size:13.4px;font-weight:300;line-height:18px;color:var(--body);width:690px;letter-spacing:.3px}
.content em{font-style:italic;font-weight:400;color:var(--ink)}
.foot-brand{left:82px;top:1036px;font-size:30px;color:#111;display:flex;align-items:center;gap:6px}
.foot-name{left:81px;top:1084px;font-size:15px;font-weight:600;color:#111}
.footer{left:0;top:1144px;width:1039px;height:56px;background:var(--footer)}
.footer span{position:absolute;top:23px;font-size:11px;color:var(--footer-text);font-weight:300}
.foot-icon{position:absolute;top:20px;width:14px;height:14px;border-radius:2px;background:var(--icon)}
</style>
</head>
<body>
<div class="abs header"></div>
<div class="abs brand"><span>Kelva</span><span class="brand-dot"></span></div>

<svg class="abs social-top" style="left:860px" viewBox="0 0 17 17"><rect width="17" height="17" fill="#3b5998"/></svg>
<svg class="abs social-top" style="left:889px" viewBox="0 0 17 17"><rect width="17" height="17" fill="#2ba9e1"/></svg>
<svg class="abs social-top" style="left:917px" viewBox="0 0 17 17"><rect width="17" height="17" fill="#e8583c"/></svg>

<nav class="nav">
  <a style="left:362px">HOME</a>
  <a class="active" style="left:421px">STUDIO</a>
  <a style="left:486px">SUPER SENIOR DAYS</a>
  <a style="left:630px">BOOK IT!</a>
  <a style="left:703px">ORDERING</a>
  <a style="left:788px">SPORTS</a>
  <a style="left:854px">CONTACT US</a>
</nav>

<div class="abs dropdown">
  <a class="current" style="top:18px">Sitting Fees</a>
  <a style="top:44px">Specials</a>
  <a style="top:70px">Family Pricing Gulid</a>
  <a style="top:96px">Seinor Pricing Gulid</a>
</div>

<div class="abs tagline">LIVE THIS MOMENT FOREVER</div>
<div class="abs follow">Follow us on Picturely<span class="follow-square"></span></div>
<div class="abs cta cta-top">Click here to book your<br><b>KELVA EXPERIENCE</b></div>

<h1 class="abs page-title">SPECIALS - FEBRUARY 2015</h1>

<main class="abs content">
  <h2 class="section-title" style="top:322px">HS Seniors</h2>
  <p style="top:373px">75% Off Senior Sessions and 8 Free wallets - Exp 2/28/15</p>
  <p style="top:422px"><em>Signature Session</em> - $200 (On Sale for Only $50 if you are photographed by February 28th) - 60 minute session in studio with up to 3 outfits and 8 Free Wallets.</p>
  <p style="top:489px"><em>Select Session</em> - $300 (On Sale for Only $75 if you are photographed by February 28th!) - 2 hour session in studio and on location with up to 5 outfits and 8 Free Wallets.</p>
  <h2 class="section-title" style="top:569px">Family and Children</h2>
  <p style="top:620px">$39 Grand Opening Portrait Special - Exp 2/28/15 (A $149 Value!)</p>
  <p style="top:669px">Includes: Studio Portrait Session With At least 20 images to choose from, One Free 8x10, and 20% Off Additional Prints for orders placed within 2 weeks of Portrait Session, AND digital file if you mention this listing or received an email.</p>
  <h2 class="section-title" style="top:768px">2011, 2012 and 2013 Old Files</h2>
  <p style="top:818px">$149 per file</p>
  <p style="top:867px">20% discount on total if you buy 5 or more.</p>
  <p style="top:917px">2014 file may be sold upon request with a $1000 sale, all balance must be paid.</p>
</main>

<div class="abs foot-brand"><span>Kelva</span><span class="brand-dot" style="width:16px;height:16px"></span></div>
<div class="abs foot-name">Kelva Prints</div>
<div class="abs cta cta-foot">Click here to book your<br><b>KELVA EXPERIENCE</b></div>

<footer class="abs footer">
  <span style="left:83px">© 2015 Kelva Prints. All rights reserved</span>
  <span style="left:340px">Legal Notice</span>
  <span style="left:438px">Terms &amp; Conditions</span>
  <i class="foot-icon" style="left:703px;background:#2ba9e1"></i>
  <i class="foot-icon" style="left:732px"></i>
  <i class="foot-icon" style="left:761px"></i>
  <i class="foot-icon" style="left:790px"></i>
  <i class="foot-icon" style="left:819px"></i>
  <i class="foot-icon" style="left:848px"></i>
  <i class="foot-icon" style="left:877px"></i>
  <i class="foot-icon" style="left:906px"></i>
  <i class="foot-icon" style="left:935px"></i>
</footer>
</body>
</html>
```